Vitamin Business Needs a Label Design

Hello. We are high-quality/healthy vitamin/supplement company, and we are in need of a Label design for a vitamin bottle.
Bottle will be either white or brown color. Label size will be 74mm*220mm. Please pick one logo from the attachments(you may use new design for the logo if you'd like to). On the front, please put two icon graphics(like certified organic sticker on food products) for "Kosher Certified" and "Vegetable Capsules". I attached sample of icon for your reference. I'm attaching files for the information. I will also put some example label designs on the brief page. Please let me know if you have any question. Thank you so much for the works!

Industry/Entity Type

Business

Font styles to use
Serif
Sans Serif

Requirements
Must have
• Information on the files. I may put barcode later, so if possible, please leave a space for barcode. Thank you.
Nice to have
• White or Ivory color for the label background would be nice. But you may use different color if you'd like to. For your information, I prefer logo 2 over logo 1, but you can use any logo as long as the design looks great.
Should not have
• Please do not use sample icon or use icon from online. It is because there may be copyright issues. For color, please do not use dark colors for label background color. (if it looks very good, then its okay).

```html
<!DOCTYPE html>
<html lang="en">
<head>
<meta charset="utf-8">
<title>Verdavita Multivitamin Label</title>
<link href="https://fonts.googleapis.com/css2?family=Merriweather:wght@700&family=Open+Sans:wght@700&family=Raleway:wght@300&display=swap" rel="stylesheet">
<style>
  :root {
    --page: #e6ece7;
    --teal: #9cc3b9;
    --paper: #f4f8f7;
    --ink: #5a574a;
    --ink-dark: #3f3d34;
    --leaf-green: #9ccc3c;
    --leaf-dark: #3f8f3a;
    --mint: #a6dfb0;
    --lime: #c9e878;
    --yellow: #e8f283;
    --badge: #7dbb45;
  }
  html, body {
    margin: 0;
    width: 1200px;
    height: 1200px;
    overflow: hidden;
    background: var(--page);
  }
  .label {
    position: absolute;
    left: 187px;
    top: 92px;
    width: 826px;
    height: 1016px;
    background: var(--paper);
    overflow: hidden;
    transform: scale(1.15);
    transform-origin: center center;
    box-shadow: 0 6px 24px rgba(40, 70, 50, 0.18);
  }
  .top-band {
    position: absolute;
    left: 0; top: 0;
    width: 100%;
    height: 372px;
    background: var(--teal);
  }
  .kosher-badge {
    position: absolute;
    left: 40px;
    top: 32px;
    width: 150px;
    height: 200px;
    border-radius: 26px;
    background: var(--badge);
  }
  .category {
    position: absolute;
    right: 36px;
    top: 92px;
    margin: 0;
    text-align: right;
    font-family: "Merriweather", Georgia, serif;
    font-weight: 700;
    font-size: 42px;
    line-height: 46px;
    color: var(--ink);
  }
  .base-tint {
    position: absolute;
    left: 0; bottom: 0;
    width: 100%;
    height: 240px;
    background: linear-gradient(to bottom,
      rgba(166, 223, 176, 0) 0%,
      var(--mint) 38%,
      var(--lime) 72%,
      var(--yellow) 100%);
  }
  .brand {
    position: absolute;
    left: 0; right: 0;
    top: 470px;
    margin: 0;
    text-align: center;
    font-family: "Open Sans", Arial, sans-serif;
    font-weight: 700;
    font-size: 112px;
    line-height: 120px;
    letter-spacing: -5px;
    color: var(--ink);
  }
  .descriptor {
    position: absolute;
    left: 0; right: 0;
    top: 600px;
    margin: 0;
    text-align: center;
    font-family: "Raleway", Arial, sans-serif;
    font-weight: 300;
    font-size: 38px;
    word-spacing: 40px;
    color: var(--ink);
  }
  .benefits {
    position: absolute;
    left: 40px;
    top: 688px;
    margin: 0;
    padding: 0;
    list-style: none;
    font-family: "Raleway", Arial, sans-serif;
    font-weight: 300;
    font-size: 34px;
    line-height: 46.5px;
    color: var(--ink);
  }
  .veg-badge {
    position: absolute;
    left: 550px;
    top: 735px;
    width: 252px;
    height: 112px;
  }
  .veg-badge .veg-top {
    font-family: "Merriweather", Georgia, serif;
    font-weight: 700;
    fill: var(--ink);
  }
  .veg-badge .veg-bottom {
    font-family: "Open Sans", Arial, sans-serif;
    font-weight: 700;
    fill: var(--ink);
  }
  .count {
    position: absolute;
    right: 34px;
    top: 866px;
    margin: 0;
    font-family: "Raleway", Arial, sans-serif;
    font-weight: 300;
    font-size: 36px;
    color: var(--ink-dark);
  }
</style>
</head>
<body>
  <main class="label">
    <div class="top-band"></div>
    <div class="kosher-badge" role="img" aria-label="Kosher certification badge"></div>
    <p class="category">Dietary<br>Supplement</p>

    <div class="base-tint" role="img" aria-label="Soft green and yellow decorative waves along the base of the label"></div>

    <h1 class="brand">Verdavita</h1>
    <p class="descriptor">MULTIVITAMIN MULTIMINERAL</p>

    <ul class="benefits">
      <li>Essential support for:</li>
      <li>Overall Health</li>
      <li>Immune System</li>
      <li>Energy</li>
      <li>Metabolism</li>
    </ul>

    <svg class="veg-badge" viewBox="0 0 252 112" aria-label="Vegetable capsules">
      <rect x="2" y="2" width="248" height="108" rx="54" fill="var(--leaf-green)"/>
      <path d="M200 2 A54 54 0 0 1 200 110 Z" fill="var(--leaf-dark)"/>
      <text class="veg-top" x="104" y="50" text-anchor="middle" font-size="28" textLength="164" lengthAdjust="spacingAndGlyphs">VEGETABLE</text>
      <text class="veg-bottom" x="104" y="86" text-anchor="middle" font-size="26" textLength="150" lengthAdjust="spacingAndGlyphs">CAPSULES</text>
    </svg>

    <p class="count">180 Capsules</p>
  </main>
</body>
</html>
```